Motor Vault Website - Part of the Brantley Group

A complimentary website is required for the launch of a 'Motor Vault' - a new service launched by industry renowned BRANTLEY. Motor Vault is an industry-first brand that designs and builds unique subterranean car parks for private residential homes in London and the influential counties within the UK. Please see here the direction of a new BRANTLEY Website - we would like Motor Vault to be complimentary and sit alongside BRANTLEY harmoniously - https://www.brantleyhq.example/brantley-nu-staging Brantley have some images, but whilst more professional images are in production - we have also attached pixmoor photos- named clearly as pixmoor. **Attached files include JPEG, .eps of logo and Brantley library images and Pixmoor Library Images - two versions of logo dependent on background colour. - Website needs to be sleek, chic and masculine.- Colour Palette - Grey/ Black/ White - Same visiual journey as Brantley website- Required areas within the sit include - About Us / Our Work / Contact Page

Target Market(s)

Luxury
Men

Number of Pages Required

2 page

Font styles to use
Sans Serif

Colors
e8e8e8
757575
1b1b1b
000000
9d9d9d
cbcbcb
f5f5f5

Requirements
Must have
• Complimentary of this site - https://www.brantleyhq.example/brantley-nu-staging
Should not have
• Colour

```html
<!DOCTYPE html>
<html lang="en">
<head>
<meta charset="utf-8">
<title>Motor Vault – Part of the Brantley Group</title>
<link href="https://fonts.googleapis.com/css2?family=Montserrat:wght@400;500;600;700;800&family=Lato:wght@400;700&display=swap" rel="stylesheet">
<style>
  :root{
    --white:#ffffff;
    --paper:#f5f5f5;
    --mist:#e8e8e8;
    --silver:#cbcbcb;
    --ash:#9d9d9d;
    --grey:#757575;
    --coal:#1b1b1b;
    --black:#000000;
    --navy:#15151f;
  }
  *{box-sizing:border-box;margin:0;padding:0}
  html,body{width:1200px;height:2616px;overflow:hidden}
  body{position:relative;font-family:'Lato',sans-serif;color:var(--coal);background:var(--white)}
  .abs{position:absolute}

  .section-title{position:absolute;left:0;width:1200px;text-align:center;font-family:'Montserrat',sans-serif;font-weight:800;font-size:20px;letter-spacing:.5px}
  .title-rule{position:absolute;left:545px;width:110px;height:12px}

  /* Hero */
  .hero{position:absolute;left:0;top:0;width:1200px;height:472px;background:radial-gradient(ellipse at 60% 40%,#6a6a6a 0%,#2e2e2e 45%,#0c0c0c 100%);overflow:hidden}
  .hero-photo{position:absolute;inset:0}
  .nav{position:absolute;left:250px;top:20px;width:700px;height:56px}
  .nav-bg{position:absolute;inset:0}
  .brand{position:absolute;display:flex;align-items:center;gap:8px;font-family:'Montserrat',sans-serif;font-weight:700;letter-spacing:.5px;white-space:nowrap}
  .brand-mark{width:14px;height:14px;background:currentColor}
  .brand-tag{position:absolute;font-family:'Lato',sans-serif;font-size:6px;letter-spacing:1px;text-transform:uppercase;white-space:nowrap}
  .nav-links{position:absolute;left:358px;top:20px;display:flex;gap:40px;font-family:'Montserrat',sans-serif;font-size:12px;color:var(--grey)}
  .nav-links .active{color:var(--coal);position:relative}
  .nav-links .active::after{content:"";position:absolute;left:0;right:0;top:25px;height:4px;background:var(--coal)}
  .hero-title{position:absolute;top:215px;left:0;width:1200px;text-align:center;font-family:'Montserrat',sans-serif;font-weight:400;font-size:32px;color:var(--white)}
  .hero-title strong{font-weight:800}
  .hero-sub{position:absolute;top:258px;left:0;width:1200px;text-align:center;font-family:'Montserrat',sans-serif;font-size:20px;color:var(--white)}
  .btn{position:absolute;display:flex;align-items:center;justify-content:center;border-radius:12px;font-family:'Montserrat',sans-serif;font-size:10px;font-weight:600}
  .btn-light{background:var(--white);color:var(--coal)}
  .btn-dark{background:var(--coal);color:var(--white)}

  /* About */
  .about{position:absolute;left:0;top:472px;width:1200px;height:355px;background:linear-gradient(135deg,var(--paper),var(--white) 60%,var(--mist));overflow:hidden}
  .ghost-word{position:absolute;font-family:'Montserrat',sans-serif;font-weight:800;color:rgba(0,0,0,.05);letter-spacing:4px;white-space:nowrap}
  .about-text{position:absolute;left:628px;top:122px;width:340px;font-size:9.5px;line-height:17.5px;color:var(--grey)}
  .about-text b{color:var(--coal)}
  .about-text p+p{margin-top:17px}

  /* Work */
  .work{position:absolute;left:0;top:827px;width:1200px;height:753px;background:linear-gradient(180deg,#1a1a26,var(--navy) 50%,#101018);overflow:hidden}
  .work-tile{position:absolute;width:290px;height:192px;border:1px solid var(--ash)}
  .work-label{position:absolute;width:290px;text-align:center;font-family:'Montserrat',sans-serif;font-size:11px;letter-spacing:.5px;color:var(--white)}
  .work-label span{position:relative;display:inline-block;padding:5px 8px}
  .work-label span::before,.work-label span::after{content:"";position:absolute;width:8px;height:8px}
  .work-label span::before{left:0;top:0;border-left:2px solid var(--white);border-top:2px solid var(--white)}
  .work-label span::after{right:0;bottom:0;border-right:2px solid var(--white);border-bottom:2px solid var(--white)}
  .work-highlight{position:absolute;background:rgba(157,157,157,.75)}

  /* Accreditations */
  .accred{position:absolute;left:0;top:1580px;width:1200px;height:188px;background:var(--mist)}
  .badge{position:absolute;top:60px;width:142px;height:75px;background:var(--paper)}
  .badge i{position:absolute;left:36px;top:20px;width:70px;height:35px;border-radius:6px;background:var(--silver)}

  /* News */
  .news{position:absolute;left:0;top:1768px;width:1200px;height:392px;background:var(--white)}
  .news-head{position:absolute;left:250px;top:145px;width:290px;font-family:'Montserrat',sans-serif;font-size:11.5px;font-weight:500;line-height:16px;text-transform:uppercase}
  .news-body{position:absolute;left:250px;top:188px;width:275px;font-size:11.5px;line-height:15.5px;color:var(--grey);letter-spacing:.3px}

  /* Contact */
  .contact{position:absolute;left:0;top:2160px;width:1200px;height:456px;background:radial-gradient(ellipse at 50% 40%,#1e1e1e,var(--black) 70%);color:var(--white)}
  .field-label{position:absolute;left:270px;font-size:9px;display:flex;align-items:center;white-space:nowrap}
  .field{position:absolute;left:308px;width:214px;height:22px;border:2px solid var(--white);border-radius:11px}
  .icon{position:absolute;left:250px;width:12px;height:12px}
  .info{position:absolute;left:765px;font-size:9px;line-height:14px;white-space:nowrap}
  .info-rule{position:absolute;left:765px;width:140px;height:1px;background:var(--grey)}
  .social{position:absolute;top:2455px;width:13px;height:13px;background:var(--ash)}
  .copyright{position:absolute;left:250px;top:2601px;font-size:6.5px;letter-spacing:.3px;text-transform:uppercase;white-space:nowrap}
</style>
</head>
<body>

<!-- Hero -->
<header class="hero">
  <div class="hero-photo" role="img" aria-label="Black and white photograph of a worker in a hard hat welding inside a timber-propped basement excavation"></div>
  <svg class="abs" style="left:0;top:0" width="1200" height="472" aria-hidden="true">
    <polygon points="0,250 140,0 210,0 0,380" fill="rgba(255,255,255,.12)"/>
    <polygon points="1150,0 1200,0 1200,90 920,472 880,472" fill="rgba(255,255,255,.35)"/>
  </svg>
  <nav class="nav">
    <svg class="nav-bg" width="700" height="56" aria-hidden="true"><polygon points="22,0 700,0 678,56 0,56" fill="#ffffff"/></svg>
    <div class="brand" style="left:40px;top:13px;font-size:20px;color:var(--coal)"><span class="brand-mark"></span>MOTOR VAULT</div>
    <div class="brand-tag" style="left:62px;top:38px;color:var(--grey)">Part of the Brantley Group</div>
    <div class="nav-links">
      <span class="active">Home</span><span>About Us</span><span>Our Work</span><span>Contact</span>
    </div>
  </nav>
  <h1 class="hero-title">Welcome to <strong>MOTOR VAULT</strong></h1>
  <p class="hero-sub">London's Most Experienced</p>
  <a class="btn btn-light" style="left:553px;top:303px;width:100px;height:24px">Contact US</a>
</header>

<!-- About -->
<section class="about">
  <div class="ghost-word" style="left:-20px;top:20px;font-size:130px">MOTOR</div>
  <div class="ghost-word" style="left:960px;top:150px;font-size:130px">VAULT</div>
  <h2 class="section-title" style="top:56px">ABOUT US</h2>
  <svg class="title-rule" style="top:82px" viewBox="0 0 110 12" aria-hidden="true"><line x1="0" y1="7" x2="42" y2="7" stroke="#1b1b1b" stroke-width="1.5" stroke-dasharray="4 3"/><line x1="68" y1="7" x2="110" y2="7" stroke="#1b1b1b" stroke-width="1.5" stroke-dasharray="4 3"/><circle cx="55" cy="6" r="4" fill="none" stroke="#1b1b1b" stroke-width="1.3"/></svg>
  <div class="abs" style="left:193px;top:82px;width:80px;height:50px;background:var(--black)"></div>
  <div class="abs" style="left:451px;top:272px;width:78px;height:50px;background:var(--black)"></div>
  <div class="abs" role="img" aria-label="Photograph of an empty concrete underground car park tunnel" style="left:220px;top:108px;width:283px;height:187px;background:radial-gradient(ellipse at 50% 50%,#d0d0d0,#4a4a4a 40%,#151515 90%);border:2px solid var(--white)"></div>
  <div class="abs" style="left:503px;top:200px;width:95px;height:2px;background:var(--coal)"></div>
  <div class="abs" style="left:596px;top:135px;width:6px;height:130px;border-radius:3px;background:var(--coal)"></div>
  <div class="about-text">
    <p>Today, <b>Motor Vault</b> designs and builds hundreds of <b>Unique Subterranean Car Parks</b> for private residential homes in London and the influential counties within the UK.</p>
    <p>With an exceptional track record for delivering projects on time and in budget, Motor Vault offers the best value in this highly specialised field.<br>Motor Vault operates a dependable, financially strong and leading London construction business which has been awarded <b>PSBA plus membership</b>.<br>Motor Vault is the trusted partner for some of <b>London's most noteworthy architects and property developers.</b></p>
  </div>
</section>

<!-- Our Work -->
<section class="work">
  <svg class="abs" style="left:0;top:0" width="1200" height="753" aria-hidden="true">
    <line x1="0" y1="70" x2="1200" y2="70" stroke="#5a5a66" stroke-width="1" opacity=".6"/>
    <line x1="700" y1="160" x2="1200" y2="160" stroke="#6a6a76" stroke-width="2" opacity=".5"/>
    <line x1="0" y1="440" x2="1200" y2="440" stroke="#4a4a56" stroke-width="2" opacity=".5"/>
    <line x1="0" y1="690" x2="1200" y2="690" stroke="#5a5a66" stroke-width="1" opacity=".5"/>
  </svg>
  <div class="ghost-word" style="left:1030px;top:590px;font-size:38px;line-height:42px;color:rgba(255,255,255,.3)">MOTOR<br>VAULT</div>
  <h2 class="section-title" style="top:56px;color:var(--white)">OUR WORK</h2>
  <svg class="title-rule" style="top:82px" viewBox="0 0 110 12" aria-hidden="true"><line x1="0" y1="7" x2="42" y2="7" stroke="#fff" stroke-width="1.5" stroke-dasharray="4 3"/><line x1="68" y1="7" x2="110" y2="7" stroke="#fff" stroke-width="1.5" stroke-dasharray="4 3"/><circle cx="55" cy="6" r="4" fill="none" stroke="#fff" stroke-width="1.3"/></svg>

  <div class="work-highlight" style="left:450px;top:122px;width:310px;height:283px"></div>

  <div class="work-tile" role="img" aria-label="Photograph of a finished underground car park with timber cladding" style="left:133px;top:133px;background:linear-gradient(135deg,#cfcfcf,#3a3a3a 55%,#111)"></div>
  <div class="work-tile" role="img" aria-label="Photograph of temporary steel propping during demolition works" style="left:460px;top:133px;background:radial-gradient(ellipse at 50% 30%,#e0e0e0,#4a4a4a 45%,#101010)"></div>
  <div class="work-tile" role="img" aria-label="Photograph of a completed basement construction corridor" style="left:783px;top:133px;background:radial-gradient(ellipse at 50% 50%,#f0f0f0,#5a5a5a 35%,#141414 85%)"></div>
  <div class="work-label" style="left:133px;top:358px"><span>CAR PARKINGS</span></div>
  <div class="work-label" style="left:460px;top:358px"><span>TEMPORARY WORKS &amp; DEMOLITION</span></div>
  <div class="work-label" style="left:783px;top:358px"><span>BASEMENT CONSTRUCTION</span></div>

  <div class="work-tile" role="img" aria-label="Photograph looking up at structural steel beams" style="left:133px;top:420px;background:linear-gradient(160deg,#eaeaea,#7a7a7a 40%,#1a1a1a)"></div>
  <div class="work-tile" role="img" aria-label="Photograph of light shining into a reinforced concrete ground works site" style="left:460px;top:420px;background:radial-gradient(ellipse at 55% 20%,#ffffff,#6a6a6a 30%,#0a0a0a 80%)"></div>
  <div class="work-tile" role="img" aria-label="Photograph of an excavator working on a shell and core basement" style="left:783px;top:420px;background:linear-gradient(180deg,#4a4a4a,#9a9a9a 45%,#2a2a2a)"></div>
  <div class="work-label" style="left:133px;top:646px"><span>STRUCTURAL ALTERATIONS</span></div>
  <div class="work-label" style="left:460px;top:646px"><span>GROUND WORKS &amp; RC FRAMES</span></div>
  <div class="work-label" style="left:783px;top:646px"><span>SHELL &amp; CORE</span></div>
</section>

<!-- Accreditations -->
<section class="accred" aria-label="Accreditations">
  <svg class="abs" style="left:248px;top:82px" width="16" height="30" aria-hidden="true"><polyline points="14,2 3,15 14,28" fill="none" stroke="#757575" stroke-width="2"/></svg>
  <div class="badge" style="left:287px"><i></i></div>
  <div class="badge" style="left:448px"><i></i></div>
  <div class="badge" style="left:612px"><i></i></div>
  <div class="badge" style="left:772px"><i></i></div>
  <svg class="abs" style="left:934px;top:82px" width="16" height="30" aria-hidden="true"><polyline points="2,2 13,15 2,28" fill="none" stroke="#1b1b1b" stroke-width="2"/></svg>
</section>

<!-- Latest News -->
<section class="news">
  <h2 class="section-title" style="top:58px">LATEST NEWS</h2>
  <svg class="title-rule" style="top:84px" viewBox="0 0 110 12" aria-hidden="true"><line x1="0" y1="7" x2="42" y2="7" stroke="#1b1b1b" stroke-width="1.5" stroke-dasharray="4 3"/><line x1="68" y1="7" x2="110" y2="7" stroke="#1b1b1b" stroke-width="1.5" stroke-dasharray="4 3"/><circle cx="55" cy="6" r="4" fill="none" stroke="#1b1b1b" stroke-width="1.3"/></svg>
  <h3 class="news-head">Typical timelines for London basement construction projects.</h3>
  <p class="news-body">The most common question from Motor Vault basement clients in London is 'how long will it take?'. There is no simple answer as each basement conversion project is unique. Whether you're an architect designing a basement for a client or you're contemplating a basement...</p>
  <a class="btn btn-dark" style="left:250px;top:307px;width:100px;height:22px">Read More</a>
  <div class="abs" style="left:596px;top:163px;width:6px;height:115px;border-radius:3px;background:var(--coal)"></div>
  <div class="abs" style="left:602px;top:220px;width:86px;height:2px;background:var(--coal)"></div>
  <div class="abs" role="img" aria-label="Photograph of workers in a basement site lit by a shaft of daylight" style="left:688px;top:132px;width:262px;height:176px;background:radial-gradient(ellipse at 45% 30%,#f2f2f2,#6a6a6a 35%,#0e0e0e 85%)"></div>
</section>

<!-- Contact -->
<section class="contact">
  <h2 class="section-title" style="top:54px;color:var(--white)">CONTACT US</h2>
  <svg class="title-rule" style="top:80px" viewBox="0 0 110 12" aria-hidden="true"><line x1="0" y1="7" x2="42" y2="7" stroke="#fff" stroke-width="1.5" stroke-dasharray="4 3"/><line x1="68" y1="7" x2="110" y2="7" stroke="#fff" stroke-width="1.5" stroke-dasharray="4 3"/><circle cx="55" cy="6" r="4" fill="none" stroke="#fff" stroke-width="1.3"/></svg>
</section>

<svg class="icon" style="top:2290px" viewBox="0 0 12 12" aria-hidden="true"><circle cx="6" cy="3.5" r="3" fill="#fff"/><path d="M0 12 Q6 4 12 12Z" fill="#fff"/></svg>
<div class="field-label" style="top:2294px;color:var(--white)">Name</div>
<div class="field" style="top:2287px"></div>
<svg class="icon" style="top:2325px" viewBox="0 0 12 12" aria-hidden="true"><rect x="0" y="2" width="12" height="8" fill="#fff"/><polyline points="0,2 6,7 12,2" fill="none" stroke="#000" stroke-width="1"/></svg>
<div class="field-label" style="top:2328px;color:var(--white)">Email</div>
<div class="field" style="top:2321px"></div>
<svg class="icon" style="top:2361px" viewBox="0 0 12 12" aria-hidden="true"><path d="M2 1 L4.5 1 L5.5 4 L4 5 Q5 8 7 8.5 L8 7 L11 8 L11 10.5 Q6 12 1.5 6 Q0.5 3 2 1Z" fill="#fff"/></svg>
<div class="field-label" style="top:2364px;color:var(--white)">Phone</div>
<div class="field" style="top:2357px"></div>
<div class="field-label" style="left:250px;top:2390px;color:var(--white)">Describe Your Project In a Few Sentences</div>
<div class="field" style="left:250px;top:2408px;width:272px;height:66px;border-radius:12px"></div>
<div class="field-label" style="left:250px;top:2490px;font-size:8px;color:var(--white)">We will contact you within one business day.</div>
<a class="btn btn-light" style="left:440px;top:2487px;width:82px;height:22px">Submit</a>

<div class="brand" style="left:765px;top:2284px;font-size:24px;color:var(--white)"><span class="brand-mark"></span>MOTOR VAULT</div>
<div class="brand-tag" style="left:790px;top:2313px;color:var(--ash)">Part of the Brantley Group</div>
<div class="info" style="top:2332px;color:var(--white)">Located In 48 HARROW YARD MEWS,<br>LONDON, W9 4LP</div>
<div class="info-rule" style="top:2368px"></div>
<div class="info" style="top:2377px;color:var(--white)">Email: INFO@BRANTLEYHQ.EXAMPLE</div>
<div class="info-rule" style="top:2403px"></div>
<div class="info" style="top:2412px;color:var(--white)">Tel: 0207 555 0142</div>
<div class="info-rule" style="top:2438px"></div>
<div class="social" style="left:765px" role="img" aria-label="Social profile"></div>
<div class="social" style="left:794px" role="img" aria-label="Social profile"></div>
<div class="social" style="left:823px" role="img" aria-label="Social profile"></div>
<div class="social" style="left:852px" role="img" aria-label="Social profile"></div>

<div class="abs" role="img" aria-label="Grey silhouette of a rocky ground line with a figure sitting and smoking" style="left:0;top:2530px;width:1200px;height:86px;background:linear-gradient(180deg,rgba(0,0,0,0),#3a3a3a 40%,#1b1b1b)"></div>
<div class="copyright" style="color:var(--white)">Copyright © Motor Vault 2019. Terms and Conditions | Privacy Policy</div>

</body>
</html>
```